We need a poster designed for use on facebook, as well as to print out for advertising in local noticeboards and shop windows.
The poster will advertise the Tallowbrook Turf Club 30th Anniversary Ball.
the ball will be held on the 28th April 2018 at the Tallowbrook Community Hall.
Time will be 630pm till late. Ticket Price is $120 which includes 3 course dinner, drinks on arrival and entertainment during the evening.
Additional details will need to be added to the poster at a later date.
The tallowbrook Turf Club is a horse racing club run by the community. The club has been incorporateds for 30 years. This Ball will be a celebration of that anniversary.

Target Market(s)

Middlemount Community

Industry/Entity Type

Club

Font styles to use
Serif
Decorative

Colors
1b1b1b
fbfbfb
6b449b
886aae
a64599
ffc214

Requirements
Must have
• Include
• where when time and cost
• ticket inclusions
• entertainement by Colin Verity
Nice to have
• Attached are some images for inspiration.
• It would be nice to have the race club logo included somewhere however not prominant.
Should not have
• Abstract geometriic lines
• images of people
• primary colours

```html
<!DOCTYPE html>
<html lang="en">
<head>
<meta charset="utf-8">
<title>Tallowbrook Turf Club 30th Anniversary Ball</title>
<link href="https://fonts.googleapis.com/css2?family=Cinzel:wght@400;700&family=Great+Vibes&family=Playfair+Display:wght@500;700&display=swap" rel="stylesheet">
<style>
  :root {
    --backdrop: #d9d9d9;
    --night: #171428;
    --night-deep: #0d0c18;
    --ivory: #fbfbfb;
    --gold: #ffc214;
    --gold-light: #f6dc7a;
    --gold-deep: #b8860b;
    --gold-glow: rgba(226,176,48,.42);
    --ink: #1b1b1b;
  }
  * { box-sizing: border-box; margin: 0; padding: 0; }
  html, body { width: 1200px; height: 880px; overflow: hidden; background: var(--backdrop); }
  .poster {
    position: absolute; left: 302px; top: 20px; width: 596px; height: 840px;
    background: radial-gradient(ellipse at 50% 40%, var(--night) 0%, var(--night-deep) 100%);
    color: var(--ivory); font-family: "Cinzel", serif; overflow: hidden;
  }
  .crest-ornament {
    position: absolute; left: 10px; top: 10px; width: 576px; height: 220px;
    background: radial-gradient(ellipse closest-side at 50% 55%, var(--gold-glow) 0%, rgba(226,176,48,.14) 55%, transparent 100%);
  }
  .club-seal {
    position: absolute; left: 234px; top: 40px; width: 128px; height: 128px;
    border-radius: 50%; background: var(--ivory); border: 5px solid var(--gold);
    display: flex; align-items: center; justify-content: center; text-align: center;
    font-family: "Cinzel", serif; font-weight: 700; font-size: 13px; line-height: 1.3; color: var(--ink);
  }
  .rule { position: absolute; height: 2px; background: linear-gradient(90deg, var(--gold-deep), var(--gold), var(--gold-deep)); }
  .rule.head { left: 22px; width: 552px; top: 194px; height: 3px; }
  .title-main {
    position: absolute; left: 0; width: 100%; top: 200px; text-align: center;
    font-size: 55px; font-weight: 700; letter-spacing: 2px;
  }
  .title-sub {
    position: absolute; left: 0; width: 100%; top: 270px; text-align: center;
    font-size: 42px; font-weight: 400; letter-spacing: 5px;
  }
  .flourish-left, .flourish-right {
    position: absolute; top: 320px; width: 240px; height: 150px;
    background: radial-gradient(ellipse closest-side, var(--gold-glow) 0%, rgba(226,176,48,.12) 55%, transparent 100%);
  }
  .flourish-left { left: 0; }
  .flourish-right { right: 0; }
  .anniversary-number {
    position: absolute; left: 0; width: 100%; top: 316px; text-align: center;
    font-family: "Playfair Display", serif; font-weight: 700; font-size: 150px; line-height: 1;
    color: var(--gold);
  }
  .anniversary-number sup { font-family: "Cinzel", serif; font-size: 20px; vertical-align: 30px; margin-left: 2px; }
  .event-script {
    position: absolute; left: 0; width: 100%; text-align: center;
    font-family: "Great Vibes", cursive; color: var(--gold); line-height: 1;
  }
  .event-script.first { top: 448px; font-size: 76px; }
  .event-script.second { top: 512px; font-size: 76px; }
  .stars { position: absolute; left: 238px; top: 596px; }
  .date-block { position: absolute; left: 60px; top: 642px; width: 100px; text-align: center; line-height: 1; }
  .date-block .month { font-size: 22px; }
  .date-block .day { font-family: "Playfair Display", serif; font-size: 46px; font-weight: 500; }
  .date-block .year { font-size: 23px; letter-spacing: 1px; }
  .divider { position: absolute; left: 178px; top: 640px; width: 2px; height: 92px; background: var(--gold); }
  .time-block { position: absolute; left: 190px; top: 648px; width: 120px; text-align: center; line-height: 1; }
  .time-block .start { font-size: 24px; }
  .time-block .till { font-size: 10px; margin: 8px 0; display: flex; align-items: center; justify-content: center; gap: 6px; }
  .time-block .till::before, .time-block .till::after { content: ""; width: 18px; height: 1px; background: var(--ivory); }
  .time-block .late { font-size: 33px; }
  .rule.venue { left: 62px; width: 236px; top: 745px; }
  .venue-name { position: absolute; left: 40px; width: 280px; top: 758px; text-align: center; font-size: 24px; line-height: 1.15; letter-spacing: 1px; }
  .ticket-banner {
    position: absolute; left: 336px; top: 624px; width: 210px; height: 182px;
    background: linear-gradient(135deg, var(--gold-light), var(--gold) 45%, var(--gold-deep));
    clip-path: polygon(0 0, 100% 0, 97% 50%, 100% 100%, 50% 95%, 0 100%, 3% 50%);
    color: var(--ink); text-align: center;
  }
  .ticket-banner .label { margin-top: 12px; font-size: 15px; letter-spacing: .5px; }
  .ticket-banner .price { font-family: "Playfair Display", serif; font-weight: 500; font-size: 76px; line-height: .95; }
  .ticket-banner .price sup { font-size: 32px; vertical-align: 30px; }
  .inclusions { display: flex; align-items: center; justify-content: center; gap: 8px; margin-top: 4px; text-align: left; }
  .inclusions .tag { font-size: 11px; }
  .inclusions ul { list-style: none; font-size: 9.5px; line-height: 1.5; }
  .inclusions li::before { content: "★ "; }
  .inclusions .performer { font-family: "Great Vibes", cursive; font-size: 16px; }
</style>
</head>
<body>
<main class="poster">
  <div class="crest-ornament" role="img" aria-label="Gold scrollwork arch framing the club seal"></div>
  <div class="club-seal">Tallowbrook<br>Turf Club</div>
  <div class="rule head"></div>
  <h1 class="title-main">TALLOWBROOK</h1>
  <h2 class="title-sub">TURF CLUBS</h2>
  <div class="flourish-left" role="img" aria-label="Gold swirl flourish"></div>
  <div class="flourish-right" role="img" aria-label="Gold swirl flourish"></div>
  <div class="anniversary-number">30<sup>TH</sup></div>
  <div class="event-script first">Anniversary</div>
  <div class="event-script second">Ball</div>
  <svg class="stars" width="120" height="32" viewBox="0 0 120 32" aria-hidden="true">
    <defs><path id="star" d="M0,-10 L2.9,-3.1 10,-3.1 4.3,1.2 6.5,8.1 0,3.8 -6.5,8.1 -4.3,1.2 -10,-3.1 -2.9,-3.1Z"/></defs>
    <g fill="#ffc214">
      <use href="#star" transform="translate(12,14) scale(.8)"/>
      <use href="#star" transform="translate(36,20)"/>
      <use href="#star" transform="translate(60,16) scale(1.3)"/>
      <use href="#star" transform="translate(84,20)"/>
      <use href="#star" transform="translate(108,14) scale(.8)"/>
    </g>
  </svg>
  <div class="date-block"><div class="month">APRIL</div><div class="day">28</div><div class="year">2018</div></div>
  <div class="divider"></div>
  <div class="time-block"><div class="start">6:30PM</div><div class="till">TILL</div><div class="late">LATE</div></div>
  <div class="rule venue"></div>
  <div class="venue-name">TALLOWBROOK<br>COMMUNITY HALL</div>
  <section class="ticket-banner">
    <div class="label">TICKET PRICE</div>
    <div class="price"><sup>$</sup>120</div>
    <div class="inclusions">
      <span class="tag">INCLUDES</span>
      <ul>
        <li>3 COURSE DINNER</li>
        <li>DRINKS ON ARRIVAL</li>
        <li>ENTERTAINEMENT BY<br><span class="performer">Colin Verity</span></li>
      </ul>
    </div>
  </section>
</main>
</body>
</html>
```